GLS biz card

We need a business card design for our new company based in Los Angeles called "Gold Lantern Studios". We develop film and television projects. We work with investors, financiers, film production companies, film distribution and sales companies as well as studios. We would like to incorporate our logo (see attached) on a two-sided card. We need to include: name and title, address, phone, email and company website.

Target Market(s)

Business, financial and studio clients

Industry/Entity Type

Business

Contact Information for Business Card

Two-sided. We are thinking of the logo on one side and the information on the back. Please feel free to be creative! Thanks.

Requirements
Must have
• Please include the following text information, excluding the "CAPS CATEGORY:" and please allow the ability for us to change the name, title and email address for each company employee):
• NAME & TITLE:
• Peter Harlow
• Managing Partner
• COMPANY NAME:
• GOLD LANTERN STUDIOS (please use existing logo)
• COMPANY ADDRESS:
• TKV Media Campus
• 2840 Welwood Avenue
• Tarlow Center, 4th Floor
• Manhattan Beach, CA 90271
• COMPANY PHONE NUMBER:
• 310-555-0148
• COMPANY WEBSITE ADDRESS:
• www.goldlanternstudiosgroup.example
• EMAIL ADDRESS: (only one per card)
• martin@goldlanternstudiosgroup.example
• buzzy@goldlanternstudiosgroup.example
• peter@goldlanternstudiosgroup.example

```html
<!DOCTYPE html>
<html lang="en">
<head>
<meta charset="utf-8">
<title>Gold Lantern Studios – Business Card</title>
<link href="https://fonts.googleapis.com/css2?family=Questrial&display=swap" rel="stylesheet">
<style>
  :root {
    --stage: #e6e6e6;
    --card-dark: #0b0c0e;
    --card-light: #f7f7f7;
    --accent: #4fb3cc;
    --ink: #1e1e1e;
    --muted: #d9d9d9;
  }
  * { box-sizing: border-box; margin: 0; padding: 0; }
  html, body { width: 1200px; height: 900px; overflow: hidden; }
  body {
    background: var(--stage);
    font-family: "Questrial", "Century Gothic", sans-serif;
    display: flex;
    align-items: center;
    justify-content: center;
    gap: 40px;
  }
  .card {
    width: 540px;
    height: 310px;
    border-radius: 3px;
    box-shadow: 0 10px 28px rgba(0,0,0,.22);
    position: relative;
    overflow: hidden;
    flex: none;
  }

  /* Front */
  .card-front {
    background: var(--card-dark);
    display: flex;
    flex-direction: column;
    align-items: center;
    justify-content: center;
    gap: 18px;
  }
  .brand-dot {
    width: 92px; height: 92px;
    border-radius: 50%;
    background: var(--accent);
  }
  .brand-name {
    color: var(--accent);
    font-size: 30px;
    letter-spacing: 3px;
  }
  .brand-tagline {
    color: var(--muted);
    font-size: 12px;
    letter-spacing: 3.5px;
    margin-top: -8px;
  }

  /* Back */
  .card-back {
    background: var(--card-light);
    color: var(--ink);
    padding: 28px 40px 24px;
    display: flex;
    flex-direction: column;
    align-items: center;
  }
  .person-name {
    color: var(--accent);
    font-size: 27px;
    line-height: 1.15;
    letter-spacing: 1px;
    font-weight: 700;
  }
  .person-title {
    font-size: 17px;
    line-height: 1.2;
    margin-top: 2px;
  }
  .company-blurb {
    font-size: 13.5px;
    line-height: 1.45;
    text-align: center;
    margin-top: 16px;
    max-width: 420px;
  }
  .rule {
    width: 100%;
    height: 3px;
    background: var(--accent);
    margin-top: 16px;
    flex: none;
  }
  .contact-list {
    margin-top: 12px;
    width: 100%;
    font-size: 12.5px;
    line-height: 1.4;
    display: flex;
    flex-direction: column;
    align-items: center;
    gap: 6px;
  }
  .contact-row {
    display: flex;
    align-items: center;
    white-space: nowrap;
  }
  .contact-item {
    display: flex;
    align-items: center;
    gap: 8px;
  }
  .contact-item + .contact-item {
    border-left: 2px solid var(--accent);
    margin-left: 14px;
    padding-left: 14px;
  }
  .contact-item svg { width: 14px; height: 14px; fill: var(--ink); flex: none; }
</style>
</head>
<body>

  <section class="card card-front" aria-label="Card front">
    <div class="brand-dot"></div>
    <div class="brand-name">GOLD LANTERN STUDIOS</div>
    <div class="brand-tagline">A MEDIA ENTERTAINMENT COMPANY</div>
  </section>

  <section class="card card-back" aria-label="Card back">
    <div class="person-name">PETER HARLOW</div>
    <div class="person-title">Managing Partner</div>
    <p class="company-blurb">We develop film &amp; television projects. We work with investors, financiers, film production companies, film distribution &amp; sales companies as well as studios.</p>
    <div class="rule"></div>
    <div class="contact-list">
      <div class="contact-row">
        <div class="contact-item address">
          <svg viewBox="0 0 16 16" aria-hidden="true"><path d="M8 1 0 8h2v7h4.5v-4.5h3V15H14V8h2z"/></svg>
          <span>TKV Media Campus, 2840 Welwood Avenue, Tarlow Center, 4th Floor<br>Manhattan Beach, CA 90271</span>
        </div>
      </div>
      <div class="contact-row">
        <div class="contact-item phone">
          <svg viewBox="0 0 16 16" aria-hidden="true"><path d="M1 5c0-2 3-3 7-3s7 1 7 3v1.5h-3.5V5h-7v1.5H1z"/><path d="M3 8h10l1.5 6h-13zM8 9.5a2 2 0 1 0 0 4 2 2 0 0 0 0-4z"/></svg>
          <span>310-555-0148</span>
        </div>
        <div class="contact-item email">
          <svg viewBox="0 0 16 16" aria-hidden="true"><path d="M0 3h16v1.2L8 9 0 4.2z"/><path d="M0 5.8 8 10.6l8-4.8V13H0z"/></svg>
          <span>peter@goldlanternstudiosgroup.example</span>
        </div>
      </div>
      <div class="contact-row">
        <div class="contact-item website">
          <svg viewBox="0 0 16 16" aria-hidden="true"><path d="M8 0a8 8 0 1 0 0 16A8 8 0 0 0 8 0zm0 1.5c.9 0 2 1.9 2.3 5.7H5.7C6 3.4 7.1 1.5 8 1.5zM1.6 7.2a6.5 6.5 0 0 1 3.1-4.8c-.6 1.2-1 2.9-1.1 4.8zm0 1.6h2c.1 1.9.5 3.6 1.1 4.8a6.5 6.5 0 0 1-3.1-4.8zM8 14.5c-.9 0-2-1.9-2.3-5.7h4.6c-.3 3.8-1.4 5.7-2.3 5.7zm3.3-.9c.6-1.2 1-2.9 1.1-4.8h2a6.5 6.5 0 0 1-3.1 4.8zm1.1-6.4c-.1-1.9-.5-3.6-1.1-4.8a6.5 6.5 0 0 1 3.1 4.8z"/></svg>
          <span>www.goldlanternstudiosgroup.example</span>
        </div>
      </div>
    </div>
  </section>

</body>
</html>
```